Business Cards for cafe providing speciality coffee and food

I need a business card design for my husband’s businesses. He has two cafes in Brisbane. The business name is Copperleaf Roasting House. They sell high end specialty coffee as well as breakfast and lunch. All the food is cooked fresh, in house and they have strict quality controls for their coffee. I would like the business card to feature the address for both cafes, my husband’s phone number and the business’s instagram. The address for the first is 61 Walden Crescent, Oakvale and the second is 23 Pellow Avenue, Brindlemoor. The Instagram handle is @copperleafroastinghouse and phone number is 0491362847. We already have a business logo that is attached.

Target Market(s)

All ages, higher disposable income and more likely to eat out regularly

Industry/Entity Type

Hospitality

Contact Information for Business Card

Must be suitable for both customers and suppliers

Font styles to use
Sans Serif

Colors

Designer to choose colors to be used in the design.

Requirements
Must have
• Owner’s name: Reid Castell
• Addresses of both cafes: 61 Walden Crescent, Oakvale and 23 Pellow Avenue, Brindlemoor
• Instagram handle: @copperleafroastinghouse
• Contact number: 0491362847
Nice to have
• Business logo

```html
<!DOCTYPE html>
<html lang="en">
<head>
<meta charset="utf-8">
<title>Copperleaf Roasting House – Business Card</title>
<link rel="stylesheet" href="https://fonts.googleapis.com/css2?family=Barlow+Condensed:wght@300;400;700&display=swap">
<style>
  :root {
    --card-bg: #ffffff;
    --ink: #111111;
    --ink-soft: #1a1a1a;
    --rule: #bdbdbd;
  }
  html, body {
    margin: 0;
    padding: 0;
    overflow: hidden;
    background: var(--card-bg);
  }
  .card {
    position: relative;
    width: 1200px;
    height: 706px;
    background: var(--card-bg);
    overflow: hidden;
    font-family: "Barlow Condensed", "Arial Narrow", sans-serif;
    color: var(--ink);
  }
  .brand {
    position: absolute;
    left: 0;
    width: 1224px;
    top: 206px;
    text-align: center;
    font-weight: 700;
    font-size: 44px;
    line-height: 1;
    letter-spacing: 3px;
    text-transform: uppercase;
    color: var(--ink);
    margin: 0;
  }
  .owner-name {
    position: absolute;
    left: 0;
    width: 1246px;
    top: 420px;
    text-align: center;
    margin: 0;
    font-weight: 700;
    font-size: 100px;
    line-height: 1;
    letter-spacing: 2px;
    text-transform: uppercase;
    color: var(--ink);
  }
  .owner-title {
    position: absolute;
    left: 512px;
    top: 546px;
    margin: 0;
    font-weight: 300;
    font-size: 64px;
    line-height: 1;
    letter-spacing: 3px;
    text-transform: uppercase;
    color: var(--ink-soft);
  }
  .contact {
    position: absolute;
    left: 0;
    width: 1200px;
    top: 632px;
    margin: 0;
    padding: 0;
    list-style: none;
    display: flex;
    justify-content: center;
    flex-wrap: wrap;
    gap: 6px 34px;
    font-weight: 400;
    font-size: 22px;
    line-height: 1.2;
    letter-spacing: 1px;
    color: var(--ink-soft);
  }
  .contact li {
    display: flex;
    align-items: center;
    gap: 8px;
  }
  .contact .icon {
    width: 16px;
    height: 16px;
    fill: var(--ink);
    flex: none;
  }
  .contact .break {
    flex-basis: 100%;
    height: 0;
  }
</style>
</head>
<body>
  <main class="card">
    <p class="brand">Copperleaf Roasting House</p>
    <h1 class="owner-name">Reid Castell</h1>
    <p class="owner-title">Owner</p>
    <ul class="contact">
      <li>
        <svg class="icon" viewBox="0 0 16 16" aria-hidden="true"><path d="M8 0a5.5 5.5 0 0 0-5.5 5.5C2.5 9.6 8 16 8 16s5.5-6.4 5.5-10.5A5.5 5.5 0 0 0 8 0zm0 7.6a2.1 2.1 0 1 1 0-4.2 2.1 2.1 0 0 1 0 4.2z"/></svg>
        61 Walden Crescent, Oakvale
      </li>
      <li>
        <svg class="icon" viewBox="0 0 16 16" aria-hidden="true"><path d="M8 0a5.5 5.5 0 0 0-5.5 5.5C2.5 9.6 8 16 8 16s5.5-6.4 5.5-10.5A5.5 5.5 0 0 0 8 0zm0 7.6a2.1 2.1 0 1 1 0-4.2 2.1 2.1 0 0 1 0 4.2z"/></svg>
        23 Pellow Avenue, Brindlemoor
      </li>
      <li class="break" aria-hidden="true"></li>
      <li>
        <svg class="icon" viewBox="0 0 16 16" aria-hidden="true"><path d="M3.6 0.6l2.2 3.2c.3.5.2 1.1-.2 1.5L4.4 6.4c.9 2 2.8 3.9 4.8 4.8l1.1-1.2c.4-.4 1-.5 1.5-.2l3.2 2.2c.5.3.6 1 .3 1.5l-1 1.6c-.4.6-1.1.9-1.8.8C6.8 15.1.9 9.2.1 3.4 0 2.7.3 2 .9 1.6l1.6-1c.4-.3 1-.2 1.1 0z"/></svg>
        0491362847
      </li>
      <li>@copperleafroastinghouse</li>
    </ul>
  </main>
</body>
</html>
```